Venue Booking Site

I would like a venue directory and booking website designed. The idea is that end users will come to the site to find venues for weddings, parties, events etc. They will be able to find the venue based on many criteria, the most important ones are availability and location - they will be able to see in real time which venues are available for the desired dates and areas.

Venues will be able to use the website as a reservation management tool, receive payments for bookings through the site and be able to manage bookings on the go. This will be made into an app. It needs to be developed in bootstrap. Brand name to be used: Mirqona. Venue, place and space bookings.

Target audience - end users - anyone who is looking for a venue. For Community members it will provide an easy way to find a suitable venue
Outline what dates and times the venue is available
Outline costs involved in booking the venue
Search via many other criteria
It will allow the customer to book and pay for the venue online in one smooth process

Clients: Venue managers - particularly focussing on not for profit businesses eg, GHAs, community hall managers, small business managers. These people typically use paper based systems yet and do not use websites so it needs to be very user friendly. Future growth to restaurants, pubs, event venues who have a stronger familiarity with computers and who might already use their own booking management tool - so this needs to be able to link in with their system.

What need will this meet for venue managers:
This tool provides venues with greater visibility, promotion and advertising of their venue
This allows more customers to find them and book with them
This tool will be offered to not-for-profit venue managers for free to better connect them to the community
This means greater profit for these community venues
This means more revenue and jobs created in these communities

Sample of the layout / contents attached. This is not a complete site map as yet as it is a work in progress for final pages.

Small Business

5+ page

Sans Serif

eb2027

• This is a psd file only - one template for each different section, home page, search page, detailed page view, admin back end
• does not need to be coded.
• Note, the golden lantern logo jpeg files were files we were toying with using for this project- but I am happy to use the main mirqona logo- I will let you decide.

```html
<!DOCTYPE html>
<html lang="en">
<head>
<meta charset="utf-8">
<title>Mirqona – Venue, place and space bookings</title>
<link rel="stylesheet" href="https://fonts.googleapis.com/css2?family=Lato:wght@400;700;900&family=Oswald:wght@400;500&display=swap">
<style>
:root{
  --red:#eb2027;
  --red-dark:#a80f15;
  --ink:#222;
  --text:#444;
  --muted:#666;
  --line:#d8d8d8;
  --panel:#ececec;
  --black:#111;
  --footer-top:#5a5a5a;
  --footer-bottom:#2e2e2e;
}
*{box-sizing:border-box;margin:0;padding:0}
html,body{width:965px;height:1200px;overflow:hidden;background:#fff}
body{position:relative;font-family:"Lato",Arial,sans-serif;color:var(--text)}
.abs{position:absolute}

/* top bar */
.topbar{left:0;top:0;width:965px;height:27px;background:var(--red-dark)}
.topbar-dark{left:0;top:0;width:330px;height:27px;background:#3b3b3b;clip-path:polygon(0 0,100% 0,290px 100%,0 100%)}
.topbar-mail{left:113px;top:8px}
.topbar-email{left:141px;top:6px;font-size:13px;color:#fff}
.topbar-search{left:643px;top:7px}
.topbar-phone{left:672px;top:5px}
.topbar-number{left:691px;top:3px;font-size:15px;color:#fff}
.login{left:800px;top:0;width:58px;height:27px;background:var(--black);color:#fff;font-size:16px;text-align:center;line-height:27px;letter-spacing:.5px}

/* header */
.header{left:0;top:27px;width:965px;height:68px;background:var(--red)}
.header-white{left:0;top:27px;width:390px;height:68px;background:#fff;clip-path:polygon(0 0,320px 0,385px 100%,0 100%)}
.brand{left:110px;top:41px;font-size:40px;color:var(--red);font-weight:400;letter-spacing:1px;line-height:48px}
.nav{left:414px;top:55px;display:flex;font-size:14px;font-weight:700;color:#fff}
.nav span{margin-right:0}

/* hero */
.hero{left:0;top:95px;width:965px;height:233px;background:linear-gradient(180deg,#4a2418 0%,#6e3a22 40%,#b79a86 75%,#d6cfc8 100%)}
.hero-line{left:0;top:327px;width:965px;height:4px;background:var(--red)}
.headline{color:#fff;font-weight:700;font-size:31px;letter-spacing:-.3px;background:rgba(235,32,39,.82);text-align:center;white-space:nowrap}
.headline-one{left:181px;top:172px;width:564px;height:52px;line-height:52px}
.headline-two{left:288px;top:237px;width:345px;height:50px;line-height:50px}

/* map search */
.map{left:0;top:331px;width:965px;height:235px;background:linear-gradient(180deg,#cfc7ae,#c6c4b4 60%,#bdbcae)}
.flap{top:566px;width:18px;height:42px;background:#3a3a3a}
.flap-left{left:157px;clip-path:polygon(0 0,100% 0,100% 100%,8px 100%)}
.flap-right{left:783px;clip-path:polygon(0 0,100% 0,10px 100%,0 100%)}
.search-shadow{left:220px;top:608px;width:520px;height:40px;background:radial-gradient(ellipse at 50% 0,rgba(0,0,0,.25),rgba(0,0,0,0) 70%)}
.search-card{left:174px;top:378px;width:609px;height:230px;background:var(--panel);border:1px solid #cfcfcf}
.search-tab{left:174px;top:378px;width:162px;height:33px;background:var(--black);clip-path:polygon(0 0,100% 0,80% 100%,0 100%)}
.search-title{left:193px;top:380px;font-family:"Oswald",sans-serif;font-size:20px;color:#fff;letter-spacing:.3px}
.label{font-size:13px;font-weight:700;color:#333}
.label-condensed{font-family:"Oswald",sans-serif;font-weight:400;font-size:13px;color:#111}
.field{height:25px;background:#fff;border:1px solid #d4d4d4;font-size:11px;color:#333;padding-left:6px;line-height:23px}
.field svg{position:absolute;right:8px;top:8px}
.submit{left:438px;top:583px;width:81px;height:25px;background:var(--red);color:#fff;font-weight:900;font-size:14px;text-align:center;line-height:26px;letter-spacing:.3px}

/* info cards */
.card{top:674px;width:241px;height:281px;background:#fff;border:1px solid #e0e0e0}
.card-title{font-size:18px;font-weight:700;color:#333;white-space:nowrap}
.card-title em{font-style:normal;color:var(--red)}
.card-rule{height:1px;background:#555}
.arrow-pair{left:313px;top:686px}
.thumb{border:1px solid #ddd;padding:3px;background:#fff}
.thumb div{width:100%;height:100%}
.venue-name{font-size:11px;font-weight:700;color:#222}
.venue-text{font-size:11px;color:#444;line-height:13px}
.divider{height:1px;background:#e2e2e2}
.why-text{left:368px;top:812px;width:226px;font-size:11px;line-height:19px;color:#333}
.read-more{left:368px;top:929px;font-size:11px;font-weight:700;color:var(--red)}
.venue-tile{width:70px;height:88px;background:#fff}
.venue-tile .pic{width:70px;height:60px}
.venue-tile .tag{position:absolute;left:0;top:64px;width:70px;height:22px;border:1px solid #e5a3a5;text-align:center;font-size:12px;font-weight:700;line-height:20px;color:#222}
.pager{left:712px;top:935px;width:36px;height:18px;background:var(--black)}

/* newsletter */
.newsletter{left:0;top:993px;width:965px;height:68px;background:var(--red)}
.news-icon{left:320px;top:1013px}
.news-input{left:352px;top:1013px;width:259px;height:24px;background:#fff;font-size:11px;color:#333;padding-left:8px;line-height:24px}
.news-go{left:611px;top:1013px;width:31px;height:24px;background:var(--black);color:#fff;font-weight:700;font-size:12px;text-align:center;line-height:24px}

/* footer */
.footer{left:0;top:1061px;width:965px;height:139px;background:linear-gradient(180deg,var(--footer-top),var(--footer-bottom))}
.footer-nav{top:1078px;font-size:11px;color:#eee}
.footer-info{font-size:10px;color:#eee;line-height:13px}
.copyright{left:0;top:1169px;width:965px;text-align:center;font-size:9px;color:#ddd}
</style>
</head>
<body>

<!-- top bar -->
<div class="abs topbar"></div>
<div class="abs topbar-dark"></div>
<svg class="abs topbar-mail" width="16" height="11" viewBox="0 0 16 11"><rect width="16" height="11" fill="#9a9a9a"/><path d="M0 0l8 6 8-6" stroke="#3b3b3b" stroke-width="1.4" fill="none"/></svg>
<div class="abs topbar-email">info@mirqona.com</div>
<svg class="abs topbar-search" width="13" height="13" viewBox="0 0 13 13"><circle cx="5.5" cy="5.5" r="4" stroke="#fff" stroke-width="1.8" fill="none"/><path d="M8.5 8.5l3.5 3.5" stroke="#fff" stroke-width="2"/></svg>
<svg class="abs topbar-phone" width="15" height="15" viewBox="0 0 24 24"><path fill="#fff" d="M6.6 10.8a15 15 0 006.6 6.6l2.2-2.2c.3-.3.7-.4 1-.2 1.1.4 2.3.6 3.6.6.6 0 1 .4 1 1V20c0 .6-.4 1-1 1A17 17 0 013 4c0-.6.4-1 1-1h3.5c.6 0 1 .4 1 1 0 1.3.2 2.5.6 3.6.1.3 0 .7-.2 1z"/></svg>
<div class="abs topbar-number">+123 456 7890</div>
<div class="abs login">LOGIN</div>

<!-- header -->
<div class="abs header"></div>
<div class="abs header-white"></div>
<div class="abs brand">MIRQONA</div>
<nav class="abs nav">
  <span style="width:96px">About Us</span>
  <span style="width:81px">Venue</span>
  <span style="width:129px">News &amp; Offers</span>
  <span style="width:69px">FAQ</span>
  <span>Contact Us</span>
</nav>

<!-- hero -->
<div class="abs hero" role="img" aria-label="Photograph of an elegant banquet hall with candlelit tables, white chair covers, columns and bookshelves"></div>
<div class="abs headline headline-one">THE DESTINATION OF YOUR DREAMS</div>
<div class="abs headline headline-two">IS JUST A CLICK AWAY</div>
<div class="abs hero-line"></div>

<!-- map + search -->
<div class="abs map" role="img" aria-label="Road map of a region showing towns and highways"></div>
<div class="abs flap flap-left"></div>
<div class="abs flap flap-right"></div>
<div class="abs search-shadow"></div>
<div class="abs search-card"></div>
<div class="abs search-tab"></div>
<div class="abs search-title">Find A Venue</div>

<div class="abs label" style="left:195px;top:417px">Venue Date</div>
<div class="abs field" style="left:195px;top:438px;width:187px">Please Select Date
  <svg width="16" height="14" viewBox="0 0 16 14" style="top:5px;right:5px"><rect x="1" y="2" width="14" height="11" fill="none" stroke="#444" stroke-width="1.4"/><rect x="1" y="2" width="14" height="3" fill="#444"/><g fill="#444"><rect x="4" y="7" width="2" height="2"/><rect x="7" y="7" width="2" height="2"/><rect x="10" y="7" width="2" height="2"/><rect x="4" y="10" width="2" height="2"/><rect x="7" y="10" width="2" height="2"/></g></svg>
</div>
<div class="abs label" style="left:395px;top:417px">Venue Location</div>
<div class="abs field" style="left:395px;top:438px;width:187px">Enter a State<svg width="14" height="7" viewBox="0 0 14 7"><path d="M1 1l6 5 6-5" stroke="#999" stroke-width="1.5" fill="none"/></svg></div>
<div class="abs label" style="left:596px;top:418px">Postcode</div>
<div class="abs field" style="left:591px;top:438px;width:187px"><svg width="14" height="7" viewBox="0 0 14 7"><path d="M1 1l6 5 6-5" stroke="#999" stroke-width="1.5" fill="none"/></svg></div>

<div class="abs label" style="left:195px;top:474px">Venue Capacity</div>
<div class="abs field" style="left:195px;top:495px;width:187px">Enter the number of people</div>
<div class="abs label" style="left:399px;top:476px">Keyword Search</div>
<div class="abs field" style="left:394px;top:494px;width:187px">Select from the list<svg width="14" height="7" viewBox="0 0 14 7"><path d="M1 1l6 5 6-5" stroke="#999" stroke-width="1.5" fill="none"/></svg></div>
<div class="abs label" style="left:593px;top:472px">Venue Use</div>
<div class="abs field" style="left:592px;top:493px;width:187px">Select from the list<svg width="14" height="7" viewBox="0 0 14 7"><path d="M1 1l6 5 6-5" stroke="#999" stroke-width="1.5" fill="none"/></svg></div>

<div class="abs label-condensed" style="left:196px;top:527px">Advance Search</div>
<div class="abs field" style="left:194px;top:547px;width:387px">Select from the list<svg width="14" height="7" viewBox="0 0 14 7"><path d="M1 1l6 5 6-5" stroke="#999" stroke-width="1.5" fill="none"/></svg></div>
<div class="abs submit">SUBMIT</div>

<!-- card: top venues -->
<div class="abs card" style="left:108px"></div>
<div class="abs card-title" style="left:117px;top:683px">Top <em>Venues</em></div>
<svg class="abs arrow-pair" width="26" height="12" viewBox="0 0 26 12"><path d="M8 1L3 6l5 5" stroke="#ccc" stroke-width="2" fill="none"/><path d="M18 1l5 5-5 5" stroke="#999" stroke-width="2" fill="none"/></svg>
<div class="abs card-rule" style="left:116px;top:710px;width:226px"></div>

<div class="abs thumb" style="left:116px;top:721px;width:59px;height:58px"><div role="img" aria-label="Venue interior lit in purple" style="background:linear-gradient(135deg,#2a0d4a,#7a2db0 50%,#1b0a33)"></div></div>
<div class="abs venue-name" style="left:184px;top:726px">Lorem ipsum dolor sit amet</div>
<div class="abs venue-text" style="left:184px;top:746px">Duis autem vel eum iriurein<br>dolor,sed&nbsp; nonmy</div>
<div class="abs divider" style="left:116px;top:791px;width:226px"></div>

<div class="abs thumb" style="left:116px;top:803px;width:59px;height:58px"><div role="img" aria-label="Dining hall with set tables" style="background:linear-gradient(135deg,#3a2a1e,#8b7560 55%,#d8ccbd)"></div></div>
<div class="abs venue-name" style="left:184px;top:808px">Lorem ipsum dolor sit amet</div>
<div class="abs venue-text" style="left:184px;top:828px">Duis autem vel eum iriurein<br>dolor,sed&nbsp; nonmy</div>
<div class="abs divider" style="left:116px;top:874px;width:226px"></div>

<div class="abs thumb" style="left:116px;top:886px;width:59px;height:58px"><div role="img" aria-label="Guests gathered at a party venue" style="background:linear-gradient(135deg,#5a1a10,#c0602f 55%,#e7a86a)"></div></div>
<div class="abs venue-name" style="left:184px;top:891px">Lorem ipsum dolor sit amet</div>
<div class="abs venue-text" style="left:184px;top:910px">Duis autem vel eum iriurein<br>dolor,sed&nbsp; nonmy</div>

<!-- card: why choose -->
<div class="abs card" style="left:361px"></div>
<div class="abs card-title" style="left:369px;top:683px">Why Choose <em>Mirqona</em></div>
<div class="abs card-rule" style="left:368px;top:710px;width:226px"></div>
<div class="abs thumb" style="left:368px;top:718px;width:227px;height:89px"><div role="img" aria-label="Photo of two business professionals in suits" style="background:linear-gradient(90deg,#f4f4f4,#d9dde3 40%,#2c3344 60%,#eef0f2)"></div></div>
<div class="abs why-text">Lorem Ipsum is simply dummy text o printing and typesetting industry. Lorem Ipsum&nbsp; been the industry's standard dummy text ev since the 1500s.Loream aliquipl ex ea commodo consequatn. Duis autem vel eum iriure dolor in hendreril in vulputa molestie consequat facilisi.</div>
<div class="abs read-more">Read More &raquo;</div>

<!-- card: recent searches -->
<div class="abs card" style="left:618px"></div>
<div class="abs card-title" style="left:626px;top:683px">Recent <em>Venue Search</em></div>
<div class="abs card-rule" style="left:626px;top:710px;width:226px"></div>

<div class="abs venue-tile" style="left:624px;top:725px"><div class="pic" role="img" aria-label="Venue 1 photo, purple-lit hall" style="background:linear-gradient(135deg,#1d0838,#8a2fc4 50%,#2a0b45)"></div><div class="tag">Venue 1</div></div>
<div class="abs venue-tile" style="left:702px;top:725px"><div class="pic" role="img" aria-label="Venue 2 photo, purple-lit hall" style="background:linear-gradient(135deg,#1d0838,#8a2fc4 50%,#2a0b45)"></div><div class="tag">Venue 2</div></div>
<div class="abs venue-tile" style="left:781px;top:725px"><div class="pic" role="img" aria-label="Venue 3 photo, purple-lit hall" style="background:linear-gradient(135deg,#1d0838,#8a2fc4 50%,#2a0b45)"></div><div class="tag">Venue 3</div></div>
<div class="abs venue-tile" style="left:624px;top:832px"><div class="pic" role="img" aria-label="Venue 4 photo, purple-lit hall" style="background:linear-gradient(135deg,#1d0838,#8a2fc4 50%,#2a0b45)"></div><div class="tag">Venue 4</div></div>
<div class="abs venue-tile" style="left:702px;top:832px"><div class="pic" role="img" aria-label="Venue 5 photo, purple-lit hall" style="background:linear-gradient(135deg,#1d0838,#8a2fc4 50%,#2a0b45)"></div><div class="tag">Venue 5</div></div>
<div class="abs venue-tile" style="left:781px;top:832px"><div class="pic" role="img" aria-label="Venue 6 photo, purple-lit hall" style="background:linear-gradient(135deg,#1d0838,#8a2fc4 50%,#2a0b45)"></div><div class="tag">Venue 6</div></div>

<svg class="abs pager" width="36" height="18" viewBox="0 0 36 18"><rect width="36" height="18" fill="#111"/><path d="M12 4l-5 5 5 5" stroke="#bbb" stroke-width="2.4" fill="none"/><path d="M24 4l5 5-5 5" stroke="#eb2027" stroke-width="2.4" fill="none"/></svg>

<!-- newsletter -->
<div class="abs newsletter"></div>
<svg class="abs news-icon" width="24" height="24" viewBox="0 0 24 24"><path d="M2 10l10-8 10 8v12H2z" fill="#fff"/><path d="M2 10l10 7 10-7" stroke="#eb2027" stroke-width="1.4" fill="none"/><circle cx="12" cy="9.5" r="3" stroke="#eb2027" stroke-width="1.2" fill="none"/></svg>
<div class="abs news-input">enter your email here</div>
<div class="abs news-go">GO</div>

<!-- footer -->
<footer class="abs footer"></footer>
<div class="abs footer-nav" style="left:234px">Home</div>
<div class="abs footer-nav" style="left:311px">About Us</div>
<div class="abs footer-nav" style="left:406px">Venue</div>
<div class="abs footer-nav" style="left:485px">News &amp; Offers</div>
<div class="abs footer-nav" style="left:606px">Faq</div>
<div class="abs footer-nav" style="left:674px">Contact Us</div>

<svg class="abs" style="left:248px;top:1122px" width="10" height="13" viewBox="0 0 10 13"><path d="M5 0a5 5 0 015 5c0 3.5-5 8-5 8S0 8.5 0 5a5 5 0 015-5z" fill="#fff"/><circle cx="5" cy="5" r="1.8" fill="#444"/></svg>
<div class="abs footer-info" style="left:265px;top:1121px">Contrary to popular belief, Lorem<br>Ipsum is.</div>
<svg class="abs" style="left:452px;top:1121px" width="11" height="11" viewBox="0 0 24 24"><path fill="#fff" d="M6.6 10.8a15 15 0 006.6 6.6l2.2-2.2c.3-.3.7-.4 1-.2 1.1.4 2.3.6 3.6.6.6 0 1 .4 1 1V20c0 .6-.4 1-1 1A17 17 0 013 4c0-.6.4-1 1-1h3.5c.6 0 1 .4 1 1 0 1.3.2 2.5.6 3.6.1.3 0 .7-.2 1z"/></svg>
<div class="abs footer-info" style="left:471px;top:1122px">Phone: 123 456 789</div>
<svg class="abs" style="left:602px;top:1123px" width="15" height="9" viewBox="0 0 15 9"><rect width="15" height="9" fill="#fff"/><path d="M0 0l7.5 5L15 0" stroke="#444" stroke-width="1.2" fill="none"/></svg>
<div class="abs footer-info" style="left:625px;top:1121px">info@sitename.com</div>
<div class="abs copyright">©2014 Mirqona&nbsp; All Rights Reserved</div>

</body>
</html>
```